Design a (20.4 x 10.14) Banner that says - Keep Hope Rising From Harvest Crown TV Family

We want a design (20.4 x 10.14) with the words 'Keep Hope Rising' as the main text and 'From Harvest Crown TV Family' underneath. For 'Harvest Crown TV', we'd like you to use the logo which can be found in the image attached.

The image attached is just an example but please let your creative juices flow!

Target Market(s)

Christian

Industry/Entity Type

Christian

Requirements
Must have
• Must have the words 'Keep Hope Rising' and 'From Harvest Crown TV Family'.

```html
<!DOCTYPE html>
<html lang="en">
<head>
<meta charset="utf-8">
<title>Keep Hope Rising – From Harvest Crown TV Family</title>
<link rel="stylesheet" href="https://fonts.googleapis.com/css2?family=Archivo:ital,wght@0,300;0,700;0,800;1,900&display=swap">
<style>
  :root {
    --white: #ffffff;
    --red: #e1061b;
    --navy: #1c2566;
    --band: rgba(255, 255, 255, 0.58);
    --sky-pink: #f3a7ad;
    --sky-rose: #e9808c;
    --sky-teal: #3fa7c4;
    --stone: #c4705a;
    --grass-gold: #e59b3a;
    --grass-green: #7d9a4a;
  }
  * { margin: 0; padding: 0; box-sizing: border-box; }
  html, body { width: 1200px; height: 596px; overflow: hidden; background: #ffffff; }

  .banner {
    position: relative;
    width: 1200px;
    height: 596px;
    overflow: hidden;
    font-family: "Archivo", Arial, sans-serif;
  }

  .scene-photo {
    position: absolute;
    inset: 0;
    background:
      radial-gradient(ellipse 260px 200px at 600px 200px, rgba(255, 236, 200, 0.9), rgba(255, 236, 200, 0) 70%),
      radial-gradient(ellipse 320px 200px at 1130px 170px, rgba(63, 167, 196, 0.85), rgba(63, 167, 196, 0) 75%),
      radial-gradient(ellipse 380px 170px at 920px 330px, rgba(196, 112, 90, 0.9), rgba(196, 112, 90, 0) 75%),
      linear-gradient(180deg, var(--sky-pink) 0%, var(--sky-rose) 45%, var(--grass-gold) 72%, var(--grass-green) 100%);
  }

  .headline {
    position: absolute;
    left: 0;
    top: 0;
    font-style: italic;
    font-weight: 900;
    letter-spacing: -3px;
    line-height: 1;
  }
  .headline span { position: absolute; white-space: nowrap; }
  .headline .word-keep   { left: 144px; top: 66px;  font-size: 150px; color: var(--white); }
  .headline .word-hope   { left: 196px; top: 152px; font-size: 134px; color: var(--red); }
  .headline .word-rising { left: 136px; top: 244px; font-size: 150px; color: var(--white); }

  .sign-off {
    position: absolute;
    left: 0;
    top: 488px;
    width: 1200px;
    height: 52px;
    background: var(--band);
    display: flex;
    align-items: center;
    justify-content: center;
    gap: 12px;
    color: var(--navy);
    font-size: 34px;
    letter-spacing: -0.5px;
  }
  .sign-off .from { font-weight: 300; }
  .sign-off .brand { font-weight: 800; }
  .sign-off .family { font-weight: 800; }
</style>
</head>
<body>
  <main class="banner">
    <div class="scene-photo" role="img" aria-label="Old stone chapel with a wooden cross beside it, golden tussock grass and mountains under a glowing pink and teal sunset sky"></div>

    <h1 class="headline" aria-label="Keep Hope Rising">
      <span class="word-keep">Keep</span>
      <span class="word-hope">HOPE</span>
      <span class="word-rising">Rising</span>
    </h1>

    <p class="sign-off">
      <span class="from">From</span>
      <span class="brand">Harvest Crown TV</span>
      <span class="family">Family</span>
    </p>
  </main>
</body>
</html>
```